Marwick Ostrand Law website for a law firm

modern clean website for a small boutique law firm. Based in Sacramento, CA and the Bay Area. Practice areas of Family Law, Civil litigation, and Criminal Defense. We already have a logo design as well as attorney pictures to include on page.
Would like images of California included on site.
Would like site to go with Logo that is already designed...blue/grey/white colors.

Industry/Entity Type

Law Firm

Number of Pages Required

5+ page

Requirements
Must have
• I already have several pages of content drafted. Just need the pages with images to input content. Must be clean and modern feel. Want it to reflect California and small boutique feel that is provided personalized legal attention.
• Must have a page where I can blog or post articles on.

```html
<!DOCTYPE html>
<html lang="en">
<head>
<meta charset="utf-8">
<title>Marwick Ostrand Law</title>
<link rel="stylesheet" href="https://fonts.googleapis.com/css2?family=Oswald:wght@500;600&family=Raleway:wght@300;400;600&family=Open+Sans:wght@400;600&display=swap">
<style>
:root{
  --blue:#3a8fd6;
  --blue-dark:#2a73b8;
  --footer:#3f8fd3;
  --ink:#333a40;
  --muted:#6b7177;
  --grey-band:#4a4e53;
  --grey-light:#eef0f2;
  --card:#e4e7ea;
  --white:#ffffff;
}
*{box-sizing:border-box;margin:0;padding:0}
html,body{width:694px;height:1200px;overflow:hidden}
body{font-family:"Open Sans",Arial,sans-serif;color:var(--ink);background:var(--white);position:relative}
.site-header{position:absolute;top:0;left:0;width:694px;height:58px;background:rgba(255,255,255,.92);display:flex;align-items:center;justify-content:space-between;padding:0 40px;z-index:2}
.brand{font-family:"Raleway",sans-serif;font-weight:400;font-size:20px;color:var(--ink);display:flex;align-items:center;gap:8px}
.brand-mark{width:12px;height:12px;border-radius:50%;background:var(--blue)}
.main-nav{display:flex;gap:22px;font-size:10px;text-transform:uppercase;color:var(--muted)}
.main-nav .active{color:var(--blue)}
.hero{position:absolute;top:0;left:0;width:694px;height:412px;background:linear-gradient(180deg,#f4f3ef 0%,#f6e6c8 38%,#e9c49e 55%,#6f8fb4 68%,#3f6aa8 80%,#2e4f8a 100%);text-align:center}
.hero-title{margin-top:104px;font-family:"Oswald",sans-serif;font-weight:600;font-size:31px;letter-spacing:1.5px;color:#1d2226;text-transform:uppercase}
.hero-tagline{font-family:"Raleway",sans-serif;font-size:14px;letter-spacing:1px;color:#5a6066;text-transform:uppercase;margin-top:2px}
.btn{display:inline-block;margin-top:14px;background:var(--blue);color:var(--white);font-size:11px;text-transform:uppercase;padding:8px 18px;letter-spacing:.5px}
.welcome{position:absolute;top:412px;left:0;width:694px;height:300px;background:var(--grey-light);text-align:center;padding-top:38px}
.section-title{font-family:"Raleway",sans-serif;font-weight:300;font-size:27px;letter-spacing:1px;text-transform:uppercase;color:var(--ink)}
.section-title span{color:var(--blue)}
.welcome p.lead{width:440px;margin:8px auto 0;font-size:8.5px;line-height:1.5;color:var(--muted)}
.practice{display:flex;gap:10px;width:610px;margin:22px auto 0}
.practice-card{width:145px;background:var(--card);text-align:center;padding-bottom:10px}
.practice-photo{height:78px}
.practice-card h3{font-family:"Raleway",sans-serif;font-weight:400;font-size:14px;color:var(--blue);margin:6px 0 3px}
.practice-card p{font-size:7.5px;line-height:1.5;color:var(--muted);padding:0 10px}
.call-band{position:absolute;top:730px;left:44px;width:610px;height:86px;background:var(--grey-band);display:flex;align-items:center;overflow:hidden}
.call-brand{width:250px;height:86px;flex:none;background:var(--blue);clip-path:polygon(0 0,100% 0,88% 100%,0 100%);display:flex;align-items:center;padding-left:24px;font-family:"Raleway",sans-serif;font-weight:400;font-size:21px;color:var(--white)}
.call-info{color:var(--white);padding-left:10px}
.call-row{display:flex;align-items:center;gap:8px;font-size:13px}
.call-row .label{font-family:"Raleway",sans-serif;text-transform:uppercase;letter-spacing:1px}
.call-sub{font-size:7.5px;color:#c9cdd1;margin-top:2px}
.call-mail{display:flex;align-items:center;gap:5px;font-size:8px;margin-top:4px}
.lower{position:absolute;top:842px;left:44px;width:610px;display:flex;gap:30px}
.news,.testimonial{width:290px}
.news .section-title,.testimonial .section-title{text-align:left;font-size:25px}
.news-item{display:flex;gap:8px;margin-top:10px}
.news-photo{width:70px;height:44px;flex:none}
.news-item h4{font-size:8.5px;font-weight:600;color:var(--blue)}
.news-date{font-size:7px;color:var(--muted);display:flex;align-items:center;gap:3px;margin:1px 0}
.news-item p{font-size:7.5px;line-height:1.4;color:var(--muted)}
.quote-mark{font-family:"Oswald",sans-serif;font-size:34px;line-height:1;color:var(--blue);margin-top:6px}
.testimonial p.quote{font-size:8.5px;line-height:1.55;color:var(--muted)}
.client{display:flex;align-items:center;gap:8px;margin-top:12px}
.client-photo{width:38px;height:38px;border-radius:50%}
.client-name{font-size:8px;color:var(--blue);text-transform:uppercase;font-weight:600}
.slider-nav{display:flex;gap:6px;margin-top:14px}
.slider-nav span{width:24px;height:24px;background:#8a9096;display:flex;align-items:center;justify-content:center}
.site-footer{position:absolute;top:1084px;left:0;width:694px;height:116px;background:var(--footer);color:var(--white);padding:16px 44px 0}
.footer-top{display:flex;justify-content:space-between;align-items:center;border-bottom:1px solid rgba(255,255,255,.35);padding-bottom:12px}
.footer-nav{display:flex;gap:22px;font-size:10px;text-transform:uppercase}
.social{display:flex;gap:8px}
.social span{width:22px;height:22px;border:1px solid rgba(255,255,255,.8)}
.footer-contact{display:flex;align-items:center;justify-content:space-between;margin-top:10px;font-size:8px}
.footer-contact h5{font-size:10px;font-weight:400;margin-bottom:4px}
.fc-item{display:flex;align-items:center;gap:6px}
.fc-icon{width:22px;height:22px;background:rgba(255,255,255,.2);display:flex;align-items:center;justify-content:center}
</style>
</head>
<body>
<header class="site-header">
  <div class="brand"><span class="brand-mark"></span>Marwick Ostrand</div>
  <nav class="main-nav">
    <span class="active">Home</span><span>About Us</span><span>Practice Areas</span><span>News</span><span>Contact Us</span>
  </nav>
</header>

<section class="hero" role="img" aria-label="Snow-capped California mountain at sunrise under a pale sky">
  <h1 class="hero-title">Marwick &amp; Ostrand Law</h1>
  <p class="hero-tagline">Strong reputations don't go unnoticed.</p>
  <span class="btn">Contact Us</span>
</section>

<section class="welcome">
  <h2 class="section-title">Welcome to <span>Marwick Ostrand</span></h2>
  <p class="lead">Lorem ipsum is simply dummy text of the printing and typesetting industry. Lorem ipsum has been the industry's standard dummy text ever since the 1500s, when an unknown printer took a galley of type and scrambled it to make a type specimen book.</p>
  <div class="practice">
    <article class="practice-card">
      <div class="practice-photo" role="img" aria-label="Business team meeting" style="background:linear-gradient(135deg,#b9c6d2,#7f95a8)"></div>
      <h3>Business Law</h3>
      <p>Lorem ipsum is simply dummy text of the printing and typesetting industry.</p>
    </article>
    <article class="practice-card">
      <div class="practice-photo" role="img" aria-label="Family together at home" style="background:linear-gradient(135deg,#d9c3a8,#a88f74)"></div>
      <h3>Family Law</h3>
      <p>Lorem ipsum is simply dummy text of the printing and typesetting industry.</p>
    </article>
    <article class="practice-card">
      <div class="practice-photo" role="img" aria-label="Judge's gavel on a desk" style="background:linear-gradient(135deg,#8a6a4e,#3e3128)"></div>
      <h3>Criminal Defense</h3>
      <p>Lorem ipsum is simply dummy text of the printing and typesetting industry.</p>
    </article>
    <article class="practice-card">
      <div class="practice-photo" role="img" aria-label="Immigration documents and passport" style="background:linear-gradient(135deg,#d6dadd,#9aa3ab)"></div>
      <h3>Immigration</h3>
      <p>Lorem ipsum is simply dummy text of the printing and typesetting industry.</p>
    </article>
  </div>
</section>

<section class="call-band">
  <div class="call-brand">Marwick Ostrand</div>
  <div class="call-info">
    <div class="call-row">
      <span class="label">Call us now</span>
      <svg width="18" height="18" viewBox="0 0 18 18"><circle cx="9" cy="9" r="8" fill="none" stroke="#fff" stroke-width="1.2"/><path d="M6 5.5l1.6-.4 1 2.2-1 .8a5 5 0 0 0 2.3 2.3l.8-1 2.2 1-.4 1.6c-3.4.3-6.8-3.1-6.5-6.5z" fill="#fff"/></svg>
      <span>(916) 555-0142, (925) 555-0187</span>
    </div>
    <div class="call-sub">Lorem ipsum is simply dummy text of the printing and type setting industry.</div>
    <div class="call-mail">
      <svg width="11" height="8" viewBox="0 0 11 8"><rect x=".5" y=".5" width="10" height="7" fill="none" stroke="#fff"/><path d="M.5 .5l5 4 5-4" fill="none" stroke="#fff"/></svg>
      hello@molegal.com
    </div>
  </div>
</section>

<section class="lower">
  <div class="news">
    <h2 class="section-title">Latest <span>News</span></h2>
    <article class="news-item">
      <div class="news-photo" role="img" aria-label="Lawyer reviewing papers" style="background:linear-gradient(135deg,#9fb0c0,#5d7287)"></div>
      <div><h4>Lorem ipsum is simply dummy text</h4><div class="news-date"><svg width="7" height="7" viewBox="0 0 7 7"><rect x=".5" y="1" width="6" height="5.5" fill="none" stroke="#3a8fd6"/></svg>15 August 2017</div><p>Lorem ipsum is simply dummy text of the printing and typesetting industry.</p></div>
    </article>
    <article class="news-item">
      <div class="news-photo" role="img" aria-label="Client consultation at an office table" style="background:linear-gradient(135deg,#c4ad93,#7d6753)"></div>
      <div><h4>Lorem ipsum is simply dummy text</h4><div class="news-date"><svg width="7" height="7" viewBox="0 0 7 7"><rect x=".5" y="1" width="6" height="5.5" fill="none" stroke="#3a8fd6"/></svg>15 August 2017</div><p>Lorem ipsum is simply dummy text of the printing and typesetting industry.</p></div>
    </article>
    <article class="news-item">
      <div class="news-photo" role="img" aria-label="Signing a legal document" style="background:linear-gradient(135deg,#b89a7c,#6f5843)"></div>
      <div><h4>Lorem ipsum is simply dummy text</h4><div class="news-date"><svg width="7" height="7" viewBox="0 0 7 7"><rect x=".5" y="1" width="6" height="5.5" fill="none" stroke="#3a8fd6"/></svg>15 August 2017</div><p>Lorem ipsum is simply dummy text of the printing and typesetting industry.</p></div>
    </article>
  </div>
  <div class="testimonial">
    <h2 class="section-title">Client <span>Testimonial</span></h2>
    <div class="quote-mark">&ldquo;</div>
    <p class="quote">Lorem ipsum is simply dummy text of the printing and typesetting industry. Lorem ipsum has been the industry's standard dummy text ever since the 1500s.</p>
    <div class="client">
      <div class="client-photo" role="img" aria-label="Client portrait" style="background:linear-gradient(135deg,#d8b9a0,#8c6a55)"></div>
      <span class="client-name">&mdash; Client Name</span>
    </div>
    <div class="slider-nav">
      <span><svg width="8" height="10" viewBox="0 0 8 10"><path d="M6 1L2 5l4 4" fill="none" stroke="#fff" stroke-width="1.5"/></svg></span>
      <span><svg width="8" height="10" viewBox="0 0 8 10"><path d="M2 1l4 4-4 4" fill="none" stroke="#fff" stroke-width="1.5"/></svg></span>
    </div>
  </div>
</section>

<footer class="site-footer">
  <div class="footer-top">
    <nav class="footer-nav"><span>Home</span><span>About Us</span><span>Practice Areas</span><span>News</span><span>Contact Us</span></nav>
    <div class="social"><span></span><span></span><span></span></div>
  </div>
  <div class="footer-contact">
    <div><h5>Contact us</h5>(916) 555-0142<br>(925) 555-0187</div>
    <div class="fc-item"><span class="fc-icon"><svg width="10" height="10" viewBox="0 0 18 18"><path d="M3 2l3-.8 2 4.4-2 1.6a10 10 0 0 0 4.6 4.6l1.6-2 4.4 2-.8 3C8.6 15.4 2.6 9.4 3 2z" fill="#fff"/></svg></span>(916) 555-0142</div>
    <div class="fc-item"><span class="fc-icon"><svg width="10" height="8" viewBox="0 0 11 8"><rect x=".5" y=".5" width="10" height="7" fill="none" stroke="#fff"/><path d="M.5 .5l5 4 5-4" fill="none" stroke="#fff"/></svg></span>hello@molegal.com</div>
    <div>&copy; Marwick Ostrand Law 2017. All Rights Reserved</div>
  </div>
</footer>
</body>
</html>
```